Glitch Tonic Energy Drink Website

We need a website to advertise and promote the product "Glitch Tonic". This is a product of https://www.bramblecrestco.net/glitchtonic.html but we want to move it to its own URL to promote the product. The theme needs to be extreme ports, gamer and cyber security orientated as these are our target audiences.

https://www.clipvista.example/shorts/Qp3Rt7WmZxA
https://www.clipvista.example/shorts/5Hdye2L-KNu

Target Market(s)

Extreme Sport, Online Gamers, Cyber Security Professionals

Coding

```html
<!DOCTYPE html>
<html lang="en">
<head>
<meta charset="utf-8">
<title>Glitch Tonic Energy Drink</title>
<link rel="stylesheet" href="https://fonts.googleapis.com/css2?family=Orbitron:wght@700;800&family=Ubuntu:wght@400;500;700&family=Montserrat:wght@700&display=swap">
<style>
:root{
  --red:#d3141c;
  --red-deep:#8c0a10;
  --red-dark:#3b0508;
  --black:#0b0b10;
  --ink:#111;
  --grey:#e6e6e6;
  --footer:#1c1c21;
  --white:#fff;
  --muted:#b9b9c0;
}
*{box-sizing:border-box;margin:0;padding:0}
html,body{width:1200px;height:3462px;overflow:hidden}
body{position:relative;background:var(--black);font-family:"Ubuntu",sans-serif;color:var(--white)}
a,a:visited{color:var(--white);text-decoration:none}
.abs{position:absolute}
.display{font-family:"Orbitron",sans-serif;font-weight:800;text-transform:uppercase;letter-spacing:1px}

/* hero + features */
.hero-band{left:0;top:0;width:1200px;height:1130px;
  background:radial-gradient(ellipse 700px 500px at 600px 560px,#b3121a 0%,#7d0a10 45%,transparent 80%),
  linear-gradient(180deg,#2a0306 0%,#6e080d 35%,#9c0e15 60%,#8c0a10 85%,#5a0609 100%)}
.hero-band svg{position:absolute;left:0;top:0}

.site-header{left:0;top:0;width:1200px;height:100px}
.brand{left:163px;top:34px;display:flex;align-items:center;gap:10px;font-weight:700;font-size:24px;letter-spacing:1px}
.brand .dot{width:30px;height:30px;border-radius:50%;background:var(--white)}
.main-nav{left:524px;top:44px;display:flex;gap:38px;font-size:12px;font-weight:700;text-transform:uppercase}
.cart{left:1016px;top:42px}

.hero-title{left:0;width:1200px;top:176px;text-align:center;font-size:84px;line-height:1}
.hero-sub{left:0;width:1200px;top:254px;text-align:center;font-size:46px;line-height:1}
.btn-outline{left:512px;top:314px;width:177px;height:42px;border:2px solid #c9c9c9;border-radius:21px;
  font-family:"Montserrat",sans-serif;font-weight:700;font-size:13px;letter-spacing:3px;display:flex;align-items:center;justify-content:center}
.hero-cans{left:322px;top:390px;width:558px;height:310px;border-radius:30px;
  background:radial-gradient(ellipse at 50% 45%,#e9e9ea 0%,#bdbdc2 45%,rgba(120,20,24,.4) 80%,transparent 100%)}

.scroll-hint{width:20px;left:590px}
.scroll-hint .dots{width:2px;height:28px;margin:0 auto;border-left:2px dotted #ccc}
.scroll-hint .ring{width:18px;height:18px;border:1px solid #ccc;border-radius:50%;margin:4px auto 0;display:flex;align-items:center;justify-content:center}

.features-title{left:0;width:1200px;top:800px;text-align:center;font-size:36px;line-height:1.05}
.feature{width:220px;text-align:center;top:900px}
.feature svg{display:block;margin:0 auto}
.feature h3{margin-top:20px;font-size:15px;font-weight:700;text-transform:uppercase;letter-spacing:.3px}

/* story */
.story{left:0;top:1050px;width:1200px;height:740px;background:linear-gradient(90deg,#141821 0%,#07080b 55%,#0d0d12 100%);
  clip-path:polygon(0 72px,1200px 0,1200px 736px,0 694px)}
.down-btn{left:573px;top:1059px;width:54px;height:54px;border-radius:50%;background:var(--white);display:flex;align-items:center;justify-content:center;box-shadow:0 0 12px rgba(0,0,0,.5)}
.story-figure{left:80px;top:1042px;width:323px;height:712px;border-radius:140px 140px 20px 20px;
  background:linear-gradient(180deg,#b7b7bf 0%,#8a8c96 30%,#d9a38d 50%,#2a2a30 75%,#111 100%)}
.story-title{left:504px;top:1290px;font-size:33px;line-height:1.05}
.story-copy{left:504px;top:1388px;width:556px;font-size:12.6px;line-height:21px;color:#e8e8ec}
.btn-red{background:var(--red);border-radius:22px;font-size:12.5px;font-weight:700;text-transform:uppercase;display:flex;align-items:center;justify-content:center;box-shadow:0 6px 14px rgba(211,20,28,.35)}
.story-btn{left:500px;top:1575px;width:155px;height:41px}

/* products */
.products{left:0;top:1750px;width:1200px;height:693px;background:var(--grey);clip-path:polygon(0 0,1200px 38px,1200px 693px,0 693px)}
.products-title{left:0;width:1200px;top:1880px;text-align:center;font-size:35px;line-height:1.05;color:var(--ink)}
.card{top:2004px;width:268px;height:272px}
.card .shot{position:absolute;left:0;top:0;width:241px;height:221px;
  background:radial-gradient(ellipse at 55% 55%,#e4e4e6 0%,#c6c6cb 40%,#a40f16 72%,#8a0a10 100%)}
.card .info{position:absolute;left:24px;top:146px;width:244px;height:126px;background:var(--white);padding:22px 0 0 27px}
.card h4{font-family:"Orbitron",sans-serif;font-weight:700;font-size:18px;color:var(--ink);line-height:1;text-transform:uppercase}
.card .kind{font-family:"Orbitron",sans-serif;font-weight:700;font-size:11px;color:var(--ink);text-transform:uppercase;margin-top:2px}
.card .price{color:var(--red);font-weight:700;font-size:13px;margin-top:10px}
.card .pack{color:#555;font-size:9.5px;font-weight:700;text-transform:uppercase;margin-top:6px}
.card .go{position:absolute;right:0;bottom:0;width:43px;height:38px;background:var(--ink);display:flex;align-items:center;justify-content:center}
.products-btn{left:520px;top:2339px;width:155px;height:42px}

/* promo */
.promo{left:0;top:2443px;width:1200px;height:770px;
  background:radial-gradient(ellipse 600px 420px at 760px 420px,#5a070b 0%,transparent 70%),linear-gradient(160deg,#1a0204 0%,#0c0608 50%,#2a0306 100%)}
.promo-brand{left:155px;top:2594px;width:270px;text-align:center;color:var(--red);font-family:"Orbitron",sans-serif;font-weight:800;text-transform:uppercase}
.promo-brand .name{font-size:54px;line-height:1}
.promo-brand .tag{font-size:14px;letter-spacing:14px;margin-top:8px}
.promo-cans{left:168px;top:2728px;width:397px;height:350px;border-radius:40px;
  background:radial-gradient(ellipse at 50% 50%,#e7e7ea 0%,#b8b8bd 50%,rgba(60,10,12,.4) 85%,transparent 100%)}
.promo-disc{left:524px;top:2641px;width:498px;height:498px;border-radius:50%;background:radial-gradient(circle at 50% 40%,#e52a2f 0%,#c8141b 60%,#a50e14 100%)}
.promo-figure{left:598px;top:2513px;width:343px;height:625px;border-radius:150px 150px 10px 10px;
  background:linear-gradient(180deg,#c9c9d0 0%,#9a9ca5 25%,#d8a08a 45%,#2a2a31 70%,#121216 100%)}
.promo-btn{left:179px;top:3107px;width:221px;height:54px;border-radius:27px;font-family:"Montserrat",sans-serif;font-size:16px;letter-spacing:3px}

/* footer */
.site-footer{left:0;top:3212px;width:1200px;height:250px;background:var(--footer)}
.foot-col h5{font-size:13px;font-weight:500;text-transform:uppercase;letter-spacing:.3px}
.foot-col ul{list-style:none;margin-top:14px}
.foot-col li{font-size:9.5px;font-weight:700;text-transform:uppercase;line-height:17.5px;padding-left:2px}
.foot-brand{left:540px;top:3262px;width:120px;text-align:center;font-weight:700;font-size:15px;letter-spacing:1px;line-height:1.3}
.foot-brand .mark{width:70px;height:70px;border-radius:50%;background:var(--white);margin:8px auto 0}
.socials{left:891px;top:3265px;display:flex;gap:14px}
.socials span{width:24px;height:24px;background:var(--white);border-radius:3px;display:block}
.copyright{left:173px;top:3432px;font-size:8.5px;color:#9a9aa3;letter-spacing:.3px;text-transform:uppercase}
.legal{left:860px;top:3432px;font-size:8.5px;color:#9a9aa3;display:flex;gap:10px}
</style>
</head>
<body>

<div class="abs hero-band">
  <svg width="1200" height="1130" viewBox="0 0 1200 1130" aria-hidden="true">
    <polygon points="0,300 420,520 0,780" fill="#5c060a" opacity=".55"/>
    <polygon points="1200,260 760,520 1200,820" fill="#4d0508" opacity=".5"/>
    <polygon points="0,0 1200,0 1200,180 600,330 0,160" fill="#1c0204" opacity=".55"/>
    <polygon points="300,1130 600,760 900,1130" fill="#a3101a" opacity=".25"/>
  </svg>
</div>

<header class="abs site-header">
  <a class="abs brand" href="https://www.bramblecrestco.net/glitchtonic.html"><span class="dot"></span>BRAMBLECREST</a>
  <nav class="abs main-nav">
    <span>Home</span><span>About the brand</span><span>Services section</span><span>Contact details</span>
  </nav>
  <svg class="abs cart" width="20" height="20" viewBox="0 0 20 20" aria-label="Cart">
    <path d="M3 6h11l-1 11H4z" fill="none" stroke="#fff" stroke-width="1.5"/>
    <path d="M6 6V4a2.5 2.5 0 0 1 5 0v2" fill="none" stroke="#fff" stroke-width="1.5"/>
    <circle cx="15" cy="4" r="4" fill="#d3141c"/>
    <text x="15" y="6" font-size="6" fill="#fff" text-anchor="middle" font-family="Ubuntu, sans-serif">0</text>
  </svg>
</header>

<h1 class="abs hero-title display">Glitch Tonic</h1>
<h2 class="abs hero-sub display">Energy Drink</h2>
<a class="abs btn-outline" href="#shop">SHOP NOW</a>
<div class="abs hero-cans" role="img" aria-label="Product photo: pile of Glitch Tonic cans with red energy sparks"></div>

<div class="abs scroll-hint" style="top:712px"><div class="dots"></div><div class="ring">
  <svg width="9" height="6" viewBox="0 0 9 6"><path d="M1 1l3.5 3.5L8 1" stroke="#ccc" fill="none"/></svg></div></div>

<h2 class="abs features-title display">Essential boost for<br>cyber defences</h2>

<div class="abs feature" style="left:122px">
  <svg width="90" height="70" viewBox="0 0 90 70">
    <circle cx="64" cy="32" r="17" fill="#e0161f"/>
    <rect x="18" y="28" width="44" height="26" fill="none" stroke="#fff" stroke-width="2"/>
    <circle cx="40" cy="41" r="7" fill="none" stroke="#fff" stroke-width="2"/>
    <path d="M40 37v5M26 28v-12M34 28v-16M46 28v-16M54 28v-12M14 54h62M24 54v6M56 54v6" stroke="#fff" stroke-width="2"/>
  </svg>
  <h3>Hack your limits</h3>
</div>
<div class="abs feature" style="left:366px">
  <svg width="90" height="70" viewBox="0 0 90 70">
    <circle cx="60" cy="36" r="17" fill="#e0161f"/>
    <path d="M20 8v44h20M28 14v30h14M40 30a10 10 0 1 0 0 16M50 52v12M58 52v12M66 44h-8" stroke="#fff" stroke-width="2" fill="none"/>
  </svg>
  <h3>Decode your energy</h3>
</div>
<div class="abs feature" style="left:609px">
  <svg width="90" height="70" viewBox="0 0 90 70">
    <circle cx="56" cy="32" r="17" fill="#e0161f"/>
    <path d="M40 14a13 13 0 0 0-8 23v8h16v-8a13 13 0 0 0-8-23zM34 50h12M36 55h8M40 4v4M24 20l-4-3M56 20l4-3M22 30h-6M58 30h6" stroke="#fff" stroke-width="2" fill="none"/>
  </svg>
  <h3>Zero-day energy</h3>
</div>
<div class="abs feature" style="left:842px">
  <svg width="90" height="70" viewBox="0 0 90 70">
    <circle cx="60" cy="32" r="17" fill="#e0161f"/>
    <rect x="18" y="8" width="46" height="42" fill="none" stroke="#fff" stroke-width="2"/>
    <path d="M18 16h46M24 24h14M24 30h14M24 36h10M44 24h14v10H44z" stroke="#fff" stroke-width="2" fill="none"/>
    <path d="M58 42l8 14H50z" fill="#fff"/>
  </svg>
  <h3>Breach your limits</h3>
</div>

<section class="abs story"></section>
<div class="abs story-figure" role="img" aria-label="Illustration: cyberpunk character in a respirator mask holding a can"></div>
<div class="abs down-btn"><svg width="22" height="14" viewBox="0 0 22 14"><path d="M2 2l9 9 9-9" stroke="#111" stroke-width="3" fill="none"/></svg></div>
<h2 class="abs story-title display">Essential boost<br>for cyber defences</h2>
<p class="abs story-copy">BRAMBLECREST is pioneering an innovative initiative that marries the thrill of extreme sports with the essential world of Cyber Security to heighten cyber awareness. We are excited to introduce GLITCH TONIC, an energy drink crafted for people who embrace extreme lifestyles, professionals in their own right, individuals with demanding jobs, and those required to operate at peak performance continuously, all while maintaining a commitment to a Cyber Secure lifestyle. GLITCH TONIC is designed to meet the intense demands of these dynamic environments, enhancing focus and energy to ensure that individuals are always prepared to excel and effectively tackle challenges. Dive into this bold approach to stay energized and sharp every day.</p>
<a class="abs btn-red story-btn" href="#shop">Shop online</a>

<section class="abs products"></section>
<div class="abs scroll-hint" style="top:1808px"><div class="dots" style="border-color:#555"></div><div class="ring" style="border-color:#555">
  <svg width="9" height="6" viewBox="0 0 9 6"><path d="M1 1l3.5 3.5L8 1" stroke="#555" fill="none"/></svg></div></div>
<h2 class="abs products-title display" id="shop">Energize your<br>exploits</h2>

<article class="abs card" style="left:109px">
  <div class="shot" role="img" aria-label="Product photo: box of 24 Glitch Tonic cans"></div>
  <div class="info"><h4>Glitch Tonic</h4><div class="kind">Energy Drink</div><div class="price">R 250.00 ZAR</div><div class="pack">24x units box</div>
  <span class="go"><svg width="18" height="12" viewBox="0 0 18 12"><path d="M1 6h15M11 1l5 5-5 5" stroke="#fff" stroke-width="1.6" fill="none"/></svg></span></div>
</article>
<article class="abs card" style="left:454px">
  <div class="shot" role="img" aria-label="Product photo: box of 12 Glitch Tonic cans with T-shirt"></div>
  <div class="info"><h4>Glitch Tonic</h4><div class="kind">Energy Drink</div><div class="price">R 350.00 ZAR</div><div class="pack">12x units box + T-shirt</div>
  <span class="go"><svg width="18" height="12" viewBox="0 0 18 12"><path d="M1 6h15M11 1l5 5-5 5" stroke="#fff" stroke-width="1.6" fill="none"/></svg></span></div>
</article>
<article class="abs card" style="left:798px">
  <div class="shot" role="img" aria-label="Product photo: box of 24 Glitch Tonic cans with T-shirt"></div>
  <div class="info"><h4>Glitch Tonic</h4><div class="kind">Energy Drink</div><div class="price">R 600.00 ZAR</div><div class="pack">24x units box + T-shirt</div>
  <span class="go"><svg width="18" height="12" viewBox="0 0 18 12"><path d="M1 6h15M11 1l5 5-5 5" stroke="#fff" stroke-width="1.6" fill="none"/></svg></span></div>
</article>
<a class="abs btn-red products-btn" href="#shop">Shop online</a>

<section class="abs promo"></section>
<div class="abs promo-brand"><div class="name">Rampart</div><div class="tag">Energy</div></div>
<div class="abs promo-cans" role="img" aria-label="Product photo: stacked Glitch Tonic cans"></div>
<div class="abs promo-disc"></div>
<div class="abs promo-figure" role="img" aria-label="Illustration: masked cyberpunk character raising a can"></div>
<a class="abs btn-red promo-btn" href="#shop">SHOP NOW</a>

<footer class="abs site-footer"></footer>
<div class="abs foot-col" style="left:175px;top:3260px"><h5>Locations</h5>
  <ul><li>South Africa</li><li>Europe</li><li>Middle-East</li><li>Africa</li><li>Namibia</li><li>United States</li></ul></div>
<div class="abs foot-col" style="left:319px;top:3260px"><h5>Additional services</h5>
  <ul><li>Crypto investigations</li><li>OSINT investigations</li><li>Incident first responder</li></ul></div>
<div class="abs foot-brand">BRAMBLECREST<div class="mark"></div></div>
<div class="abs foot-col" style="left:707px;top:3260px"><h5>News resources</h5>
  <ul><li>The Breach Wire</li><li>Packet Ledger</li><li>Threat Bulletin</li></ul></div>
<div class="abs socials" aria-label="Social links"><span></span><span></span><span></span><span></span></div>
<div class="abs copyright">Copyright 2024 Bramblecrest</div>
<div class="abs legal"><span>Privacy Policy</span><span>|</span><span>Terms &amp; Conditions</span></div>

</body>
</html>
```